Frostglen Fair LV, A Magical Holiday Festival

frostglenfairlv-example.com
Need to include the following:
Dates: Dec 14- Dec 30
kids 48'' and under free, presale tickets $6, glimmer pass $25(17 days pass) website: frostglenfairlv-example.com, ice skating rink, snow park, santa house, first 1000 kids will receive a gift from Santa on Christmas day.
Location: Brambleton Lodge, 4187 Quillstone Avenue.
Also need to include QRM logo and Grand Copperfield Supper Fair logo (I attached)

Industry/Entity Type

Festival

Font styles to use
Decorative

Requirements
Must have
• Date : December 14- December 30
• Location: Brambleton Lodge
Nice to have
• Santa House, christmas lights, ice skating rink, snow park

```html
<!DOCTYPE html>
<html lang="en">
<head>
<meta charset="utf-8">
<title>Frostglen Fair LV – A Magical Holiday Festival</title>
<link href="https://fonts.googleapis.com/css2?family=Berkshire+Swash&family=Cinzel:wght@700&family=Bebas+Neue&family=Roboto+Condensed:wght@400;700&display=swap" rel="stylesheet">
<style>
  :root {
    --backdrop: #e2e1e1;
    --navy-deep: #1f2660;
    --navy: #2c3580;
    --navy-light: #3a4597;
    --pink: #e2297e;
    --pink-light: #ee4f97;
    --cyan: #18a8dd;
    --sky: #5cc8f0;
    --gold: #f7c21b;
    --white: #ffffff;
    --muted: #c9cde6;
    --rule: #8088b8;
  }
  * { margin: 0; padding: 0; box-sizing: border-box; }
  html, body { width: 1067px; height: 1200px; overflow: hidden; background: var(--backdrop); }
  .poster {
    position: absolute; left: 162px; top: 70px; width: 746px; height: 1060px; overflow: hidden;
    background:
      radial-gradient(circle at 12% 8%, rgba(255,255,255,.18) 0 2px, transparent 3px),
      radial-gradient(circle at 85% 22%, rgba(255,255,255,.2) 0 2px, transparent 3px),
      radial-gradient(circle at 30% 40%, rgba(255,255,255,.15) 0 2px, transparent 3px),
      radial-gradient(circle at 92% 55%, rgba(255,255,255,.18) 0 2px, transparent 3px),
      radial-gradient(circle at 8% 70%, rgba(255,255,255,.15) 0 2px, transparent 3px),
      radial-gradient(circle at 60% 88%, rgba(255,255,255,.15) 0 2px, transparent 3px),
      radial-gradient(ellipse at 50% 40%, var(--navy-light), var(--navy) 55%, var(--navy-deep));
    font-family: "Roboto Condensed", "Arial Narrow", sans-serif; color: var(--white);
  }
  .decor { position: absolute; left: 0; top: 0; }
  .badge {
    position: absolute; left: 188px; top: 2px; width: 376px; height: 376px; border-radius: 50%;
    background: radial-gradient(circle at 45% 40%, var(--pink-light), var(--pink) 70%);
    box-shadow: 0 10px 30px rgba(0,0,0,.35);
  }
  .title { position: absolute; left: 0; width: 746px; text-align: center; font-family: "Berkshire Swash", Georgia, serif; font-size: 58px; line-height: 1; color: var(--white); text-shadow: 0 2px 4px rgba(120,0,50,.4); }
  .title-line1 { top: 118px; }
  .title-line2 { top: 168px; }
  .tagline { position: absolute; top: 224px; left: 0; width: 746px; text-align: center; font-family: "Cinzel", Georgia, serif; font-size: 15px; letter-spacing: .5px; }
  .dates { position: absolute; top: 274px; left: 0; width: 746px; text-align: center; font-family: "Bebas Neue", Impact, sans-serif; font-size: 40px; color: var(--gold); letter-spacing: .5px; }
  .venue { position: absolute; top: 430px; left: 0; width: 746px; text-align: center; font-size: 27px; color: var(--white); }
  .attraction { position: absolute; top: 510px; width: 200px; text-align: center; }
  .attraction-photo { width: 184px; height: 184px; margin: 0 auto; border-radius: 50%; border: 3px solid var(--white); box-shadow: 0 8px 16px rgba(0,0,0,.35); }
  .attraction-ring { position: absolute; left: 0; top: -4px; }
  .attraction-name { margin-top: 36px; font-family: "Bebas Neue", Impact, sans-serif; font-size: 27px; letter-spacing: .3px; }
  .photo-rink { background: linear-gradient(160deg, #dfe6ee, #9fb1c6 55%, #e9eef4); }
  .photo-park { background: radial-gradient(circle at 50% 35%, #f0a24a, #8a4b22 55%, #2b1b18); }
  .photo-santa { background: linear-gradient(180deg, #e8e4e2 0 18%, #d5333b 18% 42%, #f2efe9 42% 85%, #8a8f88 85%); }
  .prices { position: absolute; left: 66px; top: 796px; width: 246px; }
  .price-row { display: flex; justify-content: space-between; align-items: center; height: 46px; border-bottom: 1px solid var(--rule); font-size: 20px; }
  .price-row:last-child { border-bottom: none; }
  .price-row small { display: block; font-size: 12px; margin-top: -2px; }
  .price { font-family: "Bebas Neue", Impact, sans-serif; font-size: 32px; color: var(--gold); width: 60px; }
  .gift-card { position: absolute; left: 390px; top: 806px; width: 150px; height: 100px; border-radius: 8px; transform: rotate(-4deg); background: linear-gradient(135deg, #f6c8b4, #dd8f78); box-shadow: 0 6px 12px rgba(0,0,0,.35); }
  .gift-note { position: absolute; left: 533px; top: 807px; width: 164px; height: 106px; border: 1.5px solid var(--rule); border-radius: 8px; padding: 12px 10px 0 28px; font-size: 18px; line-height: 1.15; }
  .website { position: absolute; left: 66px; top: 982px; font-size: 24px; font-weight: 700; }
  .partner { position: absolute; font-family: "Roboto Condensed", "Arial Narrow", sans-serif; font-weight: 700; color: var(--white); }
  .partner-supper { left: 436px; top: 976px; width: 102px; font-size: 13px; line-height: 1.15; text-align: center; }
  .partner-divider { position: absolute; left: 545px; top: 968px; width: 1px; height: 52px; background: var(--rule); }
  .partner-qrm { left: 566px; top: 970px; width: 140px; font-size: 32px; text-align: center; letter-spacing: 2px; }
</style>
</head>
<body>
<main class="poster">
  <svg class="decor" width="746" height="1060" viewBox="0 0 746 1060" aria-hidden="true">
    <g fill="none" stroke-linecap="round">
      <path d="M150 130 A250 250 0 0 1 260 20" stroke="var(--pink)" stroke-width="7"/>
      <path d="M140 195 A250 250 0 0 1 152 135" stroke="var(--pink)" stroke-width="3"/>
      <path d="M520 10 A232 232 0 0 1 470 395" stroke="var(--pink)" stroke-width="3"/>
      <path d="M470 395 Q420 400 380 392" stroke="var(--pink)" stroke-width="3"/>
      <g stroke="var(--cyan)" stroke-width="1.5">
        <line x1="148" y1="290" x2="215" y2="245"/><line x1="154" y1="300" x2="222" y2="255"/>
        <line x1="232" y1="398" x2="300" y2="352"/><line x1="238" y1="408" x2="306" y2="362"/>
        <line x1="530" y1="110" x2="615" y2="55"/><line x1="540" y1="120" x2="615" y2="72"/>
        <line x1="480" y1="40" x2="525" y2="5"/><line x1="490" y1="48" x2="530" y2="15"/>
      </g>
    </g>
    <circle cx="549" cy="55" r="11" fill="var(--gold)"/>
    <circle cx="164" cy="200" r="4" fill="var(--pink)"/>
    <rect x="425" y="381" width="12" height="12" fill="var(--pink)" transform="rotate(45 431 387)"/>
    <rect x="470" y="362" width="8" height="8" fill="none" stroke="var(--pink)" stroke-width="2" transform="rotate(45 474 366)"/>
    <g fill="var(--white)">
      <circle cx="133" cy="160" r="2"/><circle cx="127" cy="166" r="2"/><circle cx="121" cy="172" r="2"/><circle cx="115" cy="178" r="2"/><circle cx="121" cy="184" r="2"/><circle cx="127" cy="190" r="2"/><circle cx="133" cy="196" r="2"/>
      <circle cx="143" cy="166" r="2"/><circle cx="137" cy="172" r="2"/><circle cx="131" cy="178" r="2"/><circle cx="137" cy="184" r="2"/><circle cx="143" cy="190" r="2"/>
      <circle cx="603" cy="160" r="2"/><circle cx="609" cy="166" r="2"/><circle cx="615" cy="172" r="2"/><circle cx="621" cy="178" r="2"/><circle cx="615" cy="184" r="2"/><circle cx="609" cy="190" r="2"/><circle cx="603" cy="196" r="2"/>
      <circle cx="613" cy="166" r="2"/><circle cx="619" cy="172" r="2"/><circle cx="625" cy="178" r="2"/><circle cx="619" cy="184" r="2"/><circle cx="613" cy="190" r="2"/>
    </g>
    <g fill="var(--sky)">
      <circle cx="603" cy="274" r="2.5"/><circle cx="603" cy="290" r="2.5"/><circle cx="603" cy="306" r="2.5"/><circle cx="603" cy="322" r="2.5"/><circle cx="603" cy="338" r="2.5"/><circle cx="603" cy="354" r="2.5"/><circle cx="603" cy="370" r="2.5"/>
      <circle cx="619" cy="258" r="2.5"/><circle cx="619" cy="274" r="2.5"/><circle cx="619" cy="290" r="2.5"/><circle cx="619" cy="306" r="2.5"/><circle cx="619" cy="322" r="2.5"/><circle cx="619" cy="338" r="2.5"/><circle cx="619" cy="354" r="2.5"/>
    </g>
  </svg>

  <div class="badge"></div>
  <h1>
    <span class="title title-line1">Frostglen</span>
    <span class="title title-line2">Fair LV</span>
  </h1>
  <p class="tagline">A MAGICAL HOLIDAY FESTIVAL</p>
  <p class="dates">14 - 30 December</p>

  <p class="venue">at Brambleton Lodge, 4187 Quillstone Avenue</p>

  <section class="attraction" style="left:46px">
    <svg class="attraction-ring" width="200" height="200" viewBox="0 0 200 200" aria-hidden="true"><path d="M150 18 A96 96 0 0 1 30 166" fill="none" stroke="var(--cyan)" stroke-width="9"/></svg>
    <div class="attraction-photo photo-rink" role="img" aria-label="Photo of skaters on an outdoor ice rink"></div>
    <h2 class="attraction-name">Ice Skating Rink,</h2>
  </section>
  <section class="attraction" style="left:270px">
    <svg class="attraction-ring" width="200" height="200" viewBox="0 0 200 200" aria-hidden="true"><path d="M150 18 A96 96 0 0 1 30 166" fill="none" stroke="var(--cyan)" stroke-width="9"/></svg>
    <div class="attraction-photo photo-park" role="img" aria-label="Photo of a snowy park with a bench under trees strung with warm lights"></div>
    <h2 class="attraction-name">Snow Park</h2>
  </section>
  <section class="attraction" style="left:494px">
    <svg class="attraction-ring" width="200" height="200" viewBox="0 0 200 200" aria-hidden="true"><path d="M150 18 A96 96 0 0 1 30 166" fill="none" stroke="var(--cyan)" stroke-width="9"/></svg>
    <div class="attraction-photo photo-santa" role="img" aria-label="Photo of a small red-roofed Santa house decorated with garlands"></div>
    <h2 class="attraction-name">Santa House</h2>
  </section>

  <div class="prices">
    <div class="price-row"><span>Kids 48" and under</span><span class="price">FREE</span></div>
    <div class="price-row"><span>Presale tickets</span><span class="price">$6</span></div>
    <div class="price-row"><span>Glimmer pass<small>(17 days pass)</small></span><span class="price">$25</span></div>
  </div>

  <div class="gift-card" role="img" aria-label="Illustrated Christmas gift card with Santa"></div>
  <p class="gift-note">First 1000 kids will receive a gift from Santa on Christmas day</p>

  <p class="website">www.frostglenfairlv-example.com</p>

  <p class="partner partner-supper">Grand Copperfield Supper Fair</p>
  <div class="partner-divider"></div>
  <p class="partner partner-qrm">QRM</p>
</main>
</body>
</html>
```